Your conflict - our mediation - joint conflict SOLUTION

With this flyer I am looking for conflict parties who are ready to tackle and resolve their conflict with a prospective mediator. The mediation is free because I am doing it as part of my diploma thesis. Time frame approx. 4 sessions of 2.5 hours each. The wishes and needs of both parties are listened to and “picked out”. In an open, constructive, appreciative framework, solutions are developed and negotiated together.

Target Market(s)

everyone who is ready to deal with himself and his counterpart and everyone who wants to work out a solution with the respect, openness and support of a mediator.

Requirements
Must have
• - "For my diploma thesis I am looking for conflicting parties who are willing to resolve their conflict with a mediator"
- Time frame: 4 x 2.5 hours feasible in Solothurn, Bern, Brugg
- Free of charge
- my coordinates - see business card
- more information at www.lindenhofwerk.ch
Nice to have
• the card should be based on the style of my homepage www.lindenhofwerk.ch and my business card

```html
<!DOCTYPE html>
<html lang="en">
<head>
<meta charset="utf-8">
<title>Ihr Konflikt – Mediation Flyer</title>
<link href="https://fonts.googleapis.com/css2?family=Anton&family=Montserrat:wght@400;600;700;800;900&display=swap" rel="stylesheet">
<style>
  :root {
    --page-bg: #e9e9e9;
    --paper: #ffffff;
    --purple: #4a2f63;
    --purple-soft: #6a5080;
    --green: #137043;
    --blue: #263a8f;
    --grey-band: #e2e1e3;
    --ink: #2b2b2b;
    --red: #e3161b;
  }
  * { margin: 0; padding: 0; box-sizing: border-box; }
  html, body { width: 693px; height: 1200px; overflow: hidden; }
  body { background: var(--page-bg); font-family: "Montserrat", sans-serif; position: relative; }

  .flyer {
    position: absolute; left: 16px; top: 133px;
    width: 660px; height: 934px;
    background: var(--paper);
    overflow: hidden;
    box-shadow: 0 4px 14px rgba(0,0,0,.28);
  }
  .flyer > * { position: absolute; }

  .brand-name { left: 42px; top: 58px; font-weight: 800; font-size: 30px; line-height: 36px; color: var(--purple); letter-spacing: .3px; }

  .hero-band { left: 0; top: 155px; width: 660px; height: 267px; background: var(--purple); }

  .hero-visual { left: 288px; top: -10px; width: 430px; height: 430px; }

  .headline { left: 42px; top: 170px; color: #fff; font-family: "Anton", sans-serif; font-weight: 400; line-height: 1; }
  .headline .line-1 { display: block; font-size: 76px; }
  .headline .line-2 { display: block; font-size: 58px; margin-top: 6px; }
  .subline { left: 42px; top: 320px; color: #fff; font-weight: 800; font-size: 23px; line-height: 32px; }

  .call-out { left: 37px; top: 440px; width: 600px; font-weight: 800; font-size: 20.5px; line-height: 29px; text-transform: uppercase; color: var(--ink); letter-spacing: .3px; }
  .call-out .lead { color: var(--green); }

  .details-band { left: 0; top: 553px; width: 660px; height: 267px; background: var(--grey-band); }
  .details-photo { left: 39px; top: 577px; width: 291px; height: 190px; background: linear-gradient(135deg, #3a3936 0%, #d9d5cf 45%, #bdb6ac 65%, #2f2e2c 100%); }

  .time-icon { left: 351px; top: 579px; width: 71px; height: 89px; background: var(--green); display: flex; align-items: center; justify-content: center; }
  .time-frame { left: 432px; top: 582px; font-size: 22px; line-height: 29px; color: var(--ink); font-weight: 600; }
  .time-frame .label { color: var(--purple); font-weight: 800; display: block; }
  .time-frame strong { font-weight: 800; }

  .locations { left: 358px; top: 694px; font-weight: 800; font-size: 19px; line-height: 31px; color: var(--ink); }
  .locations .place { display: inline-flex; align-items: center; gap: 4px; margin-right: 6px; }

  .price-pill { left: 155px; top: 799px; width: 454px; height: 54px; border-radius: 27px; background: var(--purple-soft); display: flex; align-items: center; padding-left: 17px; }
  .price-pill .free { background: #fff; color: var(--red); font-weight: 900; font-size: 46px; line-height: 50px; padding: 0 4px; letter-spacing: 1px; }
  .price-pill .rest { color: #fff; font-weight: 900; font-size: 38px; margin-left: 8px; letter-spacing: .5px; }

  .no-cost-icon { left: 58px; top: 777px; width: 98px; height: 98px; }

  .more-info { left: 0; top: 880px; width: 660px; text-align: center; font-size: 18px; color: #444; font-weight: 400; }
  .more-info strong { font-weight: 800; color: #111; }
</style>
</head>
<body>
  <article class="flyer">
    <p class="brand-name">Lindenhofwerk</p>

    <div class="hero-band"></div>

    <svg class="hero-visual" viewBox="0 0 430 430">
      <defs>
        <radialGradient id="heroFill" cx="55%" cy="45%" r="60%">
          <stop offset="0%" stop-color="#b88e6e"/>
          <stop offset="45%" stop-color="#6b4a35"/>
          <stop offset="100%" stop-color="#3a3b2e"/>
        </radialGradient>
      </defs>
      <circle cx="215" cy="215" r="205" fill="#f4f4f1"/>
      <circle cx="215" cy="215" r="194" fill="url(#heroFill)" role="img" aria-label="Photo: hand placing wooden blocks stacked as rising steps"/>
      <path d="M 60 90 A 200 200 0 0 0 150 410" fill="none" stroke="var(--blue)" stroke-width="6" stroke-linecap="round"/>
      <path d="M 95 50 A 205 205 0 0 1 400 110" fill="none" stroke="var(--green)" stroke-width="7" stroke-linecap="round"/>
    </svg>

    <h1 class="headline"><span class="line-1">IHR</span><span class="line-2">KONFLIKT</span></h1>
    <p class="subline">unsere Mediation -<br>gemeinsame Konflik-<br>tLÖSUNG</p>

    <p class="call-out"><span class="lead">For my diploma thesis I am looking for</span><br>conflicting parties who are willing to<br>resolve their conflict with a mediator</p>

    <div class="details-band"></div>
    <div class="details-photo" role="img" aria-label="Photo: several hands assembling puzzle pieces on a table"></div>

    <div class="time-icon">
      <svg width="44" height="44" viewBox="0 0 44 44" fill="none" stroke="#fff" stroke-width="2">
        <circle cx="22" cy="22" r="19"/>
        <path d="M22 10v12l7 5"/>
      </svg>
    </div>
    <p class="time-frame"><span class="label">Time frame:</span><strong>4 x 2.5</strong> hours<br><strong>feasible</strong></p>

    <p class="locations">
      <span class="place"><svg width="20" height="22" viewBox="0 0 20 22" fill="none" stroke="var(--green)" stroke-width="2"><path d="M10 15s-5-5-5-8.5a5 5 0 0 1 10 0C15 10 10 15 10 15z"/><circle cx="10" cy="6.5" r="1.8"/><path d="M3 17c0 2 14 2 14 0"/></svg>Solothurn,</span><span class="place"><svg width="20" height="22" viewBox="0 0 20 22" fill="none" stroke="var(--green)" stroke-width="2"><path d="M10 15s-5-5-5-8.5a5 5 0 0 1 10 0C15 10 10 15 10 15z"/><circle cx="10" cy="6.5" r="1.8"/><path d="M3 17c0 2 14 2 14 0"/></svg>Bern,</span><br>
      <span class="place"><svg width="20" height="22" viewBox="0 0 20 22" fill="none" stroke="var(--green)" stroke-width="2"><path d="M10 15s-5-5-5-8.5a5 5 0 0 1 10 0C15 10 10 15 10 15z"/><circle cx="10" cy="6.5" r="1.8"/><path d="M3 17c0 2 14 2 14 0"/></svg>Brugg</span>
    </p>

    <div class="price-pill"><span class="free">FREE</span><span class="rest">OF CHARGE</span></div>

    <svg class="no-cost-icon" viewBox="0 0 98 98">
      <circle cx="49" cy="49" r="46" fill="#fff" stroke="var(--red)" stroke-width="3"/>
      <rect x="16" y="32" width="66" height="34" rx="3" fill="#5fb543" stroke="#1f5e22" stroke-width="3"/>
      <circle cx="49" cy="49" r="9" fill="#f1c232" stroke="#1f5e22" stroke-width="2"/>
      <line x1="22" y1="76" x2="76" y2="22" stroke="var(--red)" stroke-width="6" stroke-linecap="round"/>
    </svg>

    <p class="more-info">more information at <strong>www.lindenhofwerk.ch</strong></p>
  </article>
</body>
</html>
```